Brochure design - Velto Rideshare community

We need a print ready brochure to tell drivers about the KRN community and the benefits of being a driver. We offer a alternative product to zandor and give drivers the ability to build their own customer base and build passive income. see design brief. check out our website www.krn-example.travel put in some good pics. Wanting a A4 Double sided brochure

Target Market(s)

Rideshare Drivers

Industry/Entity Type

Community

Font styles to use
Serif

Colors
00a990

Requirements
Must have
• clean design look. not too busy

```html
<!DOCTYPE html>
<html lang="en">
<head>
<meta charset="utf-8">
<title>KRN Driver Community Brochure</title>
<link href="https://fonts.googleapis.com/css2?family=Lato:wght@300;400;700;900&family=Oswald:wght@300;400;500&display=swap" rel="stylesheet">
<style>
  :root {
    --teal: #00a990;
    --teal-bright: #1fbfa8;
    --ink: #3a3a3a;
    --ink-soft: #555;
    --charcoal: #3c3c3e;
    --paper: #ffffff;
    --backdrop: #5f5f5f;
    --photo-light: #c9d3cf;
    --photo-mid: #8e9aa0;
    --muted: #b9b9b9;
  }
  * { box-sizing: border-box; margin: 0; padding: 0; }
  html, body { width: 1200px; height: 1200px; overflow: hidden; }
  body {
    background: var(--backdrop);
    font-family: "Lato", sans-serif;
    color: var(--ink);
    display: flex; align-items: center; justify-content: center;
  }
  .spread { display: flex; width: 1080px; height: 770px; box-shadow: 0 20px 40px rgba(0,0,0,.35); }
  .panel { position: relative; width: 360px; height: 100%; background: var(--paper); display: flex; flex-direction: column; overflow: hidden; }
  .panel + .panel { border-left: 1px solid #e2e2e2; }

  /* Panel 1 – driver requirements */
  .intro { padding: 30px 26px 22px; }
  .intro h3 { color: var(--teal); font-weight: 700; font-size: 15px; margin-bottom: 10px; }
  .intro p { font-size: 11px; line-height: 1.45; color: var(--ink); }
  .expect { background: var(--teal-bright); color: #fff; padding: 22px 26px 24px; }
  .expect h4 { font-size: 13px; font-weight: 700; letter-spacing: .02em; margin-bottom: 12px; }
  .expect h5 { font-size: 11.5px; font-weight: 700; margin: 8px 0 6px; }
  .expect h5::before { content: "» "; }
  .tick-list { list-style: none; }
  .tick-list li { position: relative; padding-left: 18px; font-size: 10.5px; line-height: 1.35; margin-bottom: 5px; }
  .tick-list li svg { position: absolute; left: 0; top: 2px; width: 10px; height: 10px; }
  .expect .tick-list li svg circle, .expect .tick-list li svg path { stroke: #e6fbf7; }
  .photo { flex: 1; background: linear-gradient(160deg, var(--photo-light), var(--photo-mid)); }
  .teal-strip { height: 18px; background: var(--teal-bright); }

  /* Panel 2 – join */
  .join { padding: 30px 28px 24px; display: flex; flex-direction: column; height: 100%; }
  .join .about { font-size: 10.5px; line-height: 1.45; color: var(--ink-soft); margin-bottom: 26px; }
  .join .be-part { color: var(--teal); font-size: 22px; font-weight: 400; line-height: 1.1; }
  .join .community { font-family: "Oswald", sans-serif; font-size: 24px; font-weight: 500; color: var(--ink); letter-spacing: .02em; line-height: 1.15; }
  .join .easy { color: var(--teal); font-size: 28px; font-weight: 700; line-height: 1.15; margin-bottom: 16px; }
  .steps { list-style: none; margin-bottom: 26px; }
  .steps li { display: flex; align-items: center; gap: 10px; font-size: 11px; margin-bottom: 10px; }
  .steps .num { width: 18px; height: 18px; border-radius: 50%; background: var(--teal); color: #fff; font-size: 10px; font-weight: 700; display: flex; align-items: center; justify-content: center; }
  .offer { border-top: 1px solid #d6d6d6; padding-top: 8px; display: flex; justify-content: space-between; align-items: center; }
  .offer-title { font-family: "Oswald", sans-serif; font-size: 30px; color: var(--teal); line-height: 1; }
  .offer-sub { font-size: 20px; font-weight: 700; color: var(--ink-soft); }
  .price-badge { width: 74px; height: 74px; border-radius: 50%; background: var(--teal); border: 3px solid #fff; box-shadow: 0 0 0 2px var(--teal); color: #fff; display: flex; flex-direction: column; align-items: center; justify-content: center; font-weight: 700; }
  .price-badge s { font-size: 15px; }
  .price-badge b { font-size: 17px; }
  .monthly { font-size: 14px; font-weight: 700; color: var(--ink-soft); margin-top: 6px; margin-bottom: 30px; }
  .monthly span { color: var(--teal); }
  .offer-list h4 { color: var(--teal); font-size: 14px; font-weight: 700; margin-bottom: 10px; }
  .offer-list .tick-list li { font-size: 10px; color: var(--ink-soft); }
  .offer-list .tick-list svg circle, .offer-list .tick-list svg path { stroke: var(--ink-soft); }
  .contact { margin-top: auto; display: flex; justify-content: space-between; align-items: flex-end; }
  .contact ul { list-style: none; }
  .contact li { display: flex; align-items: center; gap: 7px; font-size: 10.5px; margin-bottom: 4px; color: var(--ink); }
  .contact li svg { width: 11px; height: 11px; }
  .mini-name { font-size: 22px; font-weight: 400; color: var(--muted); letter-spacing: .06em; line-height: 1; margin-bottom: 6px; }

  /* Panel 3 – cover */
  .brand { height: 130px; display: flex; align-items: center; justify-content: center; }
  .brand-name { font-size: 44px; font-weight: 400; color: #1a1a1a; letter-spacing: .08em; line-height: 1; }
  .cover-photo { height: 360px; background: linear-gradient(160deg, #b8c2b2, #6d767b); }
  .headline { background: var(--charcoal); flex: 1; border-top: 4px solid #fff; display: flex; flex-direction: column; align-items: center; justify-content: center; text-align: center; font-family: "Oswald", sans-serif; }
  .headline .providing { color: var(--teal-bright); font-weight: 300; font-size: 32px; }
  .headline .big { color: #fff; font-weight: 400; font-size: 32px; letter-spacing: .01em; line-height: 1.15; }
  .headline .want { color: var(--teal-bright); font-weight: 300; font-size: 22px; }
  .url { height: 46px; display: flex; align-items: center; justify-content: center; font-size: 11px; letter-spacing: .3em; color: #222; }
</style>
</head>
<body>
<main class="spread">

  <section class="panel panel-requirements">
    <div class="intro">
      <h3>Interested in becoming a KRN Driver?</h3>
      <p>Are you an experienced and reliable driver? Do you have a passion for providing high quality service? Are you keen to be part of one of the world's most reputable networks of drivers? KRN has a solid network of drivers, both in Australia and internationally.</p>
    </div>
    <div class="expect">
      <h4>WHAT WE EXPECT FROM YOU :</h4>
      <h5>In order to become a KRN driver, we require:</h5>
      <ul class="tick-list">
        <li><svg viewBox="0 0 10 10"><circle cx="5" cy="5" r="4.3" fill="none" stroke-width="1"/><path d="M3 5.2l1.4 1.4L7.2 3.6" fill="none" stroke-width="1.1"/></svg>Relevant transport authority accreditation documentation.</li>
        <li><svg viewBox="0 0 10 10"><circle cx="5" cy="5" r="4.3" fill="none" stroke-width="1"/><path d="M3 5.2l1.4 1.4L7.2 3.6" fill="none" stroke-width="1.1"/></svg>Industry references - either from a client or driver.</li>
        <li><svg viewBox="0 0 10 10"><circle cx="5" cy="5" r="4.3" fill="none" stroke-width="1"/><path d="M3 5.2l1.4 1.4L7.2 3.6" fill="none" stroke-width="1.1"/></svg>Proof of business registration documentation</li>
        <li><svg viewBox="0 0 10 10"><circle cx="5" cy="5" r="4.3" fill="none" stroke-width="1"/><path d="M3 5.2l1.4 1.4L7.2 3.6" fill="none" stroke-width="1.1"/></svg>Insurance and registration paperwork</li>
      </ul>
      <h5>We also expect you to :</h5>
      <ul class="tick-list">
        <li><svg viewBox="0 0 10 10"><circle cx="5" cy="5" r="4.3" fill="none" stroke-width="1"/><path d="M3 5.2l1.4 1.4L7.2 3.6" fill="none" stroke-width="1.1"/></svg>Have a professional approach and offer friendly service.</li>
        <li><svg viewBox="0 0 10 10"><circle cx="5" cy="5" r="4.3" fill="none" stroke-width="1"/><path d="M3 5.2l1.4 1.4L7.2 3.6" fill="none" stroke-width="1.1"/></svg>Arrive at bookings on time.</li>
        <li><svg viewBox="0 0 10 10"><circle cx="5" cy="5" r="4.3" fill="none" stroke-width="1"/><path d="M3 5.2l1.4 1.4L7.2 3.6" fill="none" stroke-width="1.1"/></svg>Take the fastest route to a destination, including all tollways.</li>
        <li><svg viewBox="0 0 10 10"><circle cx="5" cy="5" r="4.3" fill="none" stroke-width="1"/><path d="M3 5.2l1.4 1.4L7.2 3.6" fill="none" stroke-width="1.1"/></svg>Dress in smart casual attire.</li>
        <li><svg viewBox="0 0 10 10"><circle cx="5" cy="5" r="4.3" fill="none" stroke-width="1"/><path d="M3 5.2l1.4 1.4L7.2 3.6" fill="none" stroke-width="1.1"/></svg>Carry bags, open doors, offer water, newspaper and minutes for your clients.</li>
        <li><svg viewBox="0 0 10 10"><circle cx="5" cy="5" r="4.3" fill="none" stroke-width="1"/><path d="M3 5.2l1.4 1.4L7.2 3.6" fill="none" stroke-width="1.1"/></svg>Always smile!</li>
      </ul>
    </div>
    <div class="photo" role="img" aria-label="Photo of a smiling driver seated at the wheel of a car"></div>
    <div class="teal-strip"></div>
  </section>

  <section class="panel panel-join">
    <div class="join">
      <p class="about">KRN is a professional, global transfer service based in Australia. No matter where in the world you are you can count on us to get you where you need to go – in style, in comfort and on time.</p>
      <div class="be-part">Be a part of</div>
      <div class="community">THE KRN COMMUNITY</div>
      <div class="easy">It is easy to join!</div>
      <ol class="steps">
        <li><span class="num">1</span>Sign up online</li>
        <li><span class="num">2</span>Upload your compliance documents.</li>
      </ol>
      <div class="offer">
        <div>
          <div class="offer-title">SPECIAL OFFER</div>
          <div class="offer-sub">Activation Fee</div>
        </div>
        <div class="price-badge"><s>$149</s><b>$ 49</b></div>
      </div>
      <div class="monthly">Monthly access fee only <span>$ 19.95</span></div>
      <div class="offer-list">
        <h4>WHAT WE OFFER</h4>
        <ul class="tick-list">
          <li><svg viewBox="0 0 10 10"><circle cx="5" cy="5" r="4.3" fill="none" stroke-width="1"/><path d="M3 5.2l1.4 1.4L7.2 3.6" fill="none" stroke-width="1.1"/></svg>Great clients, based in Australia and abroad</li>
          <li><svg viewBox="0 0 10 10"><circle cx="5" cy="5" r="4.3" fill="none" stroke-width="1"/><path d="M3 5.2l1.4 1.4L7.2 3.6" fill="none" stroke-width="1.1"/></svg>Fixed and transport pricing</li>
          <li><svg viewBox="0 0 10 10"><circle cx="5" cy="5" r="4.3" fill="none" stroke-width="1"/><path d="M3 5.2l1.4 1.4L7.2 3.6" fill="none" stroke-width="1.1"/></svg>Prompt payment</li>
          <li><svg viewBox="0 0 10 10"><circle cx="5" cy="5" r="4.3" fill="none" stroke-width="1"/><path d="M3 5.2l1.4 1.4L7.2 3.6" fill="none" stroke-width="1.1"/></svg>The ability to build up a repeat client base with clients who rate you highly.</li>
          <li><svg viewBox="0 0 10 10"><circle cx="5" cy="5" r="4.3" fill="none" stroke-width="1"/><path d="M3 5.2l1.4 1.4L7.2 3.6" fill="none" stroke-width="1.1"/></svg>Cutting edge technology to manage your booking.</li>
          <li><svg viewBox="0 0 10 10"><circle cx="5" cy="5" r="4.3" fill="none" stroke-width="1"/><path d="M3 5.2l1.4 1.4L7.2 3.6" fill="none" stroke-width="1.1"/></svg>A performance-driven incentive.</li>
          <li><svg viewBox="0 0 10 10"><circle cx="5" cy="5" r="4.3" fill="none" stroke-width="1"/><path d="M3 5.2l1.4 1.4L7.2 3.6" fill="none" stroke-width="1.1"/></svg>The more clients who rate your service, the more repeat booking you will secure</li>
          <li><svg viewBox="0 0 10 10"><circle cx="5" cy="5" r="4.3" fill="none" stroke-width="1"/><path d="M3 5.2l1.4 1.4L7.2 3.6" fill="none" stroke-width="1.1"/></svg>Build passive income from referral customers</li>
        </ul>
      </div>
      <div class="contact">
        <ul>
          <li><svg viewBox="0 0 12 12"><path d="M3 1.5l1.6 2.4-1 1.1a6 6 0 0 0 3.4 3.4l1.1-1 2.4 1.6-.8 1.6C6 10.4 1.6 6 1.4 2.3z" fill="#555"/></svg>61 000 555 0142</li>
          <li><svg viewBox="0 0 12 12"><rect x="1" y="2.5" width="10" height="7" fill="#555"/><path d="M1 2.5l5 4 5-4" fill="none" stroke="#fff" stroke-width=".9"/></svg>info@krn-example.travel</li>
          <li><svg viewBox="0 0 12 12"><circle cx="6" cy="6" r="4.8" fill="none" stroke="#555"/><path d="M1.2 6h9.6M6 1.2c-2.4 2.6-2.4 7 0 9.6M6 1.2c2.4 2.6 2.4 7 0 9.6" fill="none" stroke="#555" stroke-width=".8"/></svg>www.krn-example.travel</li>
        </ul>
        <div class="mini-name">KRN</div>
      </div>
    </div>
  </section>

  <section class="panel panel-cover">
    <div class="brand"><div class="brand-name">KRN</div></div>
    <div class="cover-photo" role="img" aria-label="Photo of a smiling driver in shirt and tie at the wheel of a bus, giving a thumbs up"></div>
    <div class="headline">
      <div class="providing">Providing</div>
      <div class="big">EXCEPTIONAL SERVICE</div>
      <div class="want">and want to be a part of</div>
      <div class="big">THE KRN COMMUNITY</div>
    </div>
    <div class="url">www.krn-example.travel</div>
    <div class="teal-strip"></div>
  </section>

</main>
</body>
</html>
```